Voltarra: Electrical Contractor flyer design.

We are looking for a sharp and professional flyer to promote the business's cost for specific jobs and to promote the business.
We are a small electrical business looking to break into the market.
Attached logo to be used and following content to be incorporated. Contact details will be given upon final flyer design.

Internal Power Points: $ 120
External Weather Proof Power Points: $150
T.V. Points: $120 (excludes aerial)
T.V. Mounting: $ 200 (Exclude Leads)
Aerials Starting From: $220 Incudes Mast
LED Down lights: $60 per unti
Ceiling Fans: $150 (Fan Excluded)
Oven & Range Hood Change Overs: $250
A.C. Install: $300
S/B Upgrade: From $600
Safety Switch Installation: $280
Phone Points: $120

Services Incude:

New home wiring
Shop & Office Fit Outs
Re - Wires
Extentions
Garden Lighting
Home Thearters
Home Automation
Power Points
Phone, Data
Feature Lighting
Lighting design and Installation
Ceiling Fans
A.C Installation
Oven & Range hood Installation

*All prices are gst inclusive
**Prices subject to change due to site access.

```html
<!DOCTYPE html>
<html lang="en">
<head>
<meta charset="utf-8">
<title>Voltarra – Electrical Contractor Flyer</title>
<link rel="stylesheet" href="https://fonts.googleapis.com/css2?family=Bebas+Neue&family=Lato:ital,wght@0,700;0,900;1,400;1,700;1,900&display=swap">
<style>
  :root {
    --orange: #f26a1b;
    --orange-light: #f7943d;
    --orange-deep: #e4560c;
    --charcoal: #3e3e40;
    --charcoal-dark: #2f2f31;
    --ink: #2b2b2b;
    --muted: #4a4a4a;
    --paper: #ffffff;
    --paper-shade: #eeeeee;
    --backdrop: #e6e4e1;
    --photo-light: #d9dde2;
    --photo-mid: #9aa6b4;
    --photo-dark: #3d4d66;
  }
  * { box-sizing: border-box; margin: 0; padding: 0; }
  html, body { width: 825px; height: 1200px; overflow: hidden; }
  body { background: var(--backdrop); position: relative; font-family: "Lato", sans-serif; }

  .flyer {
    position: absolute; left: 60px; top: 143px; width: 707px; height: 915px;
    background: linear-gradient(180deg, var(--paper) 0%, var(--paper-shade) 100%);
    overflow: hidden;
    box-shadow: 0 4px 14px rgba(0,0,0,.18);
  }
  .flyer-shapes { position: absolute; inset: 0; }

  .headline {
    position: absolute; right: 20px; top: 58px; width: 300px;
    font-family: "Bebas Neue", sans-serif; font-weight: 400; text-align: center; line-height: .95;
    white-space: nowrap;
  }
  .headline-line { display: block; color: var(--paper); font-size: 40px; letter-spacing: .3px; }
  .headline-feature { display: block; color: var(--charcoal); font-size: 66px; letter-spacing: .5px; margin: 6px 0 2px; }

  .brand {
    position: absolute; left: 436px; top: 340px; width: 240px;
    display: flex; align-items: center; gap: 12px; justify-content: center;
  }
  .brand-mark { width: 34px; height: 34px; background: var(--orange); }
  .brand-name { font-family: "Lato", sans-serif; font-weight: 900; font-size: 42px; color: var(--charcoal); letter-spacing: .5px; }

  .services { position: absolute; left: 22px; top: 405px; width: 260px; color: var(--paper); }
  .services-title { font-style: italic; font-weight: 900; font-size: 26px; margin-bottom: 8px; }
  .services-list { list-style: none; }
  .services-list li {
    font-style: italic; font-weight: 700; font-size: 14.3px; line-height: 19.5px;
    padding-left: 22px; position: relative; white-space: nowrap;
  }
  .services-list li::before {
    content: ""; position: absolute; left: 3px; top: 8px; width: 5px; height: 5px;
    border-radius: 50%; background: var(--paper);
  }

  .contact { position: absolute; left: 23px; top: 776px; width: 230px; }
  .contact-row {
    display: flex; align-items: flex-end; height: 21.5px;
    font-style: italic; font-weight: 700; font-size: 14px; color: var(--orange);
  }
  .contact-label { width: 74px; }
  .contact-line { flex: 1; border-bottom: 1px solid var(--muted); margin-bottom: 6px; }

  .pricing-note {
    position: absolute; left: 326px; top: 445px;
    font-style: italic; font-size: 17px; color: var(--muted); white-space: nowrap;
  }

  .price-table {
    position: absolute; left: 316px; top: 479px; width: 356px;
    border: 2px solid var(--orange); border-radius: 12px; overflow: hidden;
    border-collapse: separate; border-spacing: 0; background: var(--paper);
  }
  .price-table th {
    background: linear-gradient(180deg, var(--orange-light), var(--orange-deep));
    color: var(--paper); font-style: italic; font-weight: 700; font-size: 15px;
    text-align: left; height: 32px; padding: 0 16px;
  }
  .price-table td {
    font-style: italic; font-size: 11px; color: var(--ink);
    height: 24.2px; padding: 0 16px; border-top: 1px solid var(--orange); white-space: nowrap;
  }
  .price-table .col-price { width: 128px; padding-left: 6px; border-left: 1px solid var(--orange); }
  .price-table th.col-price { border-left: none; }

  .gst-note {
    position: absolute; left: 325px; top: 860px;
    font-style: italic; font-weight: 700; font-size: 24px; color: var(--paper); letter-spacing: .5px;
    white-space: nowrap;
  }
</style>
</head>
<body>
<main class="flyer">
  <svg class="flyer-shapes" width="707" height="915" viewBox="0 0 707 915">
    <defs>
      <linearGradient id="photoTone" x1="0" y1="0" x2="1" y2="1">
        <stop offset="0" stop-color="#d9dde2"/>
        <stop offset=".55" stop-color="#9aa6b4"/>
        <stop offset="1" stop-color="#3d4d66"/>
      </linearGradient>
      <linearGradient id="orangeTone" x1="0" y1="0" x2="1" y2="1">
        <stop offset="0" stop-color="#e4560c"/>
        <stop offset=".6" stop-color="#f26a1b"/>
        <stop offset="1" stop-color="#f7943d"/>
      </linearGradient>
      <linearGradient id="panelTone" x1="0" y1="0" x2="1" y2="1">
        <stop offset="0" stop-color="#e4560c"/>
        <stop offset="1" stop-color="#f7943d"/>
      </linearGradient>
    </defs>

    <path class="hero-photo" role="img" aria-label="Photo of an electrician in a hard hat and navy workwear working on a switchboard"
          fill="url(#photoTone)"
          d="M0,0 H320 C372,70 398,170 395,245 C392,310 350,365 300,400 H0 Z"/>

    <path class="hero-edge" fill="none" stroke="#3e3e40" stroke-width="7"
          d="M312,-4 C370,60 398,160 398,225 C400,250 420,262 470,262 H710"/>

    <path class="hero-swoosh" fill="url(#orangeTone)"
          d="M322,0 H707 V254 H472 C430,254 404,240 402,215 C398,140 376,60 322,0 Z"/>

    <path class="services-panel" fill="url(#panelTone)"
          d="M0,379 H262 Q282,379 282,399 V712 C282,740 262,748 230,750 C150,755 70,762 0,770 Z"/>

    <path class="footer-accent" fill="none" stroke="#f26a1b" stroke-width="4"
          d="M0,878 C150,876 250,870 300,852 C320,844 340,841 362,841 H707"/>
    <path class="footer-band" fill="#2f2f31"
          d="M0,915 V888 C160,886 262,880 310,862 C330,852 346,849 366,849 H707 V915 Z"/>
  </svg>

  <h1 class="headline">
    <span class="headline-line">Creating Impression</span>
    <span class="headline-feature">Worldwide</span>
    <span class="headline-line">With Elegance</span>
  </h1>

  <div class="brand">
    <span class="brand-mark"></span>
    <span class="brand-name">Voltarra</span>
  </div>

  <section class="services">
    <h2 class="services-title">Our services:</h2>
    <ul class="services-list">
      <li>New home wiring</li>
      <li>Shop &amp; Office Fit Outs</li>
      <li>Re - Wires</li>
      <li>Extentions</li>
      <li>Garden Lighting</li>
      <li>Home Thearters</li>
      <li>Home Automation</li>
      <li>Power Points</li>
      <li>Phone, Data</li>
      <li>Feature Lighting</li>
      <li>Lighting design and Installation</li>
      <li>Ceiling Fans</li>
      <li>A.C Installation</li>
      <li>Oven &amp; Range hood Installation</li>
    </ul>
  </section>

  <section class="contact">
    <div class="contact-row"><span class="contact-label">Email:</span><span class="contact-line"></span></div>
    <div class="contact-row"><span class="contact-label">Mobile:</span><span class="contact-line"></span></div>
    <div class="contact-row"><span class="contact-label">Website:</span><span class="contact-line"></span></div>
    <div class="contact-row"><span class="contact-label">Facebook:</span><span class="contact-line"></span></div>
  </section>

  <p class="pricing-note">Prices subject to change due to site access.</p>

  <table class="price-table">
    <thead>
      <tr><th>Points:</th><th class="col-price">Price:</th></tr>
    </thead>
    <tbody>
      <tr><td>Internal Power Points:</td><td class="col-price">$ 120</td></tr>
      <tr><td>External Weather Proof Power Points:</td><td class="col-price">$150</td></tr>
      <tr><td>T.V. Points:</td><td class="col-price">$120 (excludes aerial)</td></tr>
      <tr><td>T.V. Mounting:</td><td class="col-price">$ 200 (Exclude Leads)</td></tr>
      <tr><td>Aerials Starting From:</td><td class="col-price">$220 Incudes Mast</td></tr>
      <tr><td>LED Down lights:</td><td class="col-price">$60 per unti</td></tr>
      <tr><td>Ceiling Fans:</td><td class="col-price">$150 (Fan Excluded)</td></tr>
      <tr><td>Oven &amp; Range Hood Change Overs:</td><td class="col-price">$250</td></tr>
      <tr><td>A.C. Install:</td><td class="col-price">$300</td></tr>
      <tr><td>S/B Upgrade:</td><td class="col-price">From $600</td></tr>
      <tr><td>Safety Switch Installation:</td><td class="col-price">$280</td></tr>
      <tr><td>Phone Points:</td><td class="col-price">$120</td></tr>
    </tbody>
  </table>

  <p class="gst-note">*All prices are gst inclusive</p>
</main>
</body>
</html>
```